website redesign - bronwickhomes.com.au

need to redesign our website. we are proud of our current website but market feedback suggests that we have to tone down our quirkiness and make it look more professional to target the million dollar market.
right now we appeal to the younger generation so we have to meet somewhere in the middle.
we want to still retain our same flavour and style but need to also look a bit more professional. we need to evolve our brand to a more grown up look.
examples of standard websites include tallow estates, gant dwellings, lodger ledger, fennimore upward, dowsett

```html
<!DOCTYPE html>
<html lang="en">
<head>
<meta charset="utf-8">
<title>Bronwick Homes – Properties</title>
<link href="https://fonts.googleapis.com/css2?family=DM+Sans:wght@400;500;700&family=Caveat:wght@500&display=swap" rel="stylesheet">
<style>
:root{
  --orange:#f04e0a;
  --navy:#14213d;
  --text:#1d2438;
  --grey:#9aa0aa;
  --line:#e3e5ea;
  --soft:#f7f8fa;
  --white:#ffffff;
}
*{box-sizing:border-box;margin:0;padding:0}
html,body{width:1200px;height:2253px;overflow:hidden;background:var(--white)}
body{position:relative;font-family:"DM Sans",sans-serif;color:var(--text)}
.abs{position:absolute}
.brand{font-size:16px;font-weight:700;letter-spacing:1.5px;color:var(--navy);display:flex;align-items:center;gap:7px}
.brand-dot{width:8px;height:8px;background:var(--orange)}
.header{left:0;top:0;width:1200px;height:91px;border-bottom:1px solid #f0f1f4}
.btn-outline{border:1px solid var(--orange);color:var(--orange);font-size:12px;font-weight:500;display:flex;align-items:center;justify-content:center;border-radius:2px}
.menu-btn{width:35px;height:35px;border-radius:50%;background:var(--orange);display:flex;align-items:center;justify-content:center}
.band{left:0;top:179px;width:1200px;height:351px;background:var(--soft)}
.title{left:88px;top:252px;font-size:51px;font-weight:500;color:var(--navy);letter-spacing:-0.5px}
.tab{top:346px;width:113px;height:46px;border-radius:23px;display:flex;align-items:center;justify-content:center;gap:6px;font-size:10px;font-weight:500}
.tab.active{background:var(--orange);color:var(--white)}
.tab.plain{border:1px solid #b9bec8;color:var(--text);background:var(--white)}
.script{font-family:"Caveat",cursive;color:var(--orange)}
.card{width:304px;height:332px;background:var(--white);border:1px solid var(--line);border-radius:4px;overflow:hidden}
.photo{height:175px;position:relative}
.dots{position:absolute;left:32px;bottom:22px;display:flex;gap:4px}
.dots i{width:7px;height:7px;border-radius:50%;background:rgba(255,255,255,.7)}
.dots i:first-child{background:var(--orange)}
.card-body{padding:16px 31px 0}
.card-title{font-size:19px;font-weight:500;color:var(--navy)}
.stats{display:flex;align-items:center;margin-top:12px;font-size:15px;font-weight:500}
.stat{display:flex;align-items:center;gap:12px;width:70px}
.price{display:flex;align-items:center;gap:12px;margin-top:12px;color:var(--orange);font-size:14px;font-weight:700;padding-bottom:12px}
.card-foot{border-top:1px solid var(--line);padding:10px 31px;display:flex;align-items:center;gap:12px;font-size:11px}
.btn-solid{background:var(--orange);color:var(--white);display:flex;align-items:center;justify-content:center;gap:10px;font-weight:500}
.feature{left:0;top:1364px;width:601px;height:455px;background:var(--soft)}
.feature-photo{left:601px;top:1364px;width:599px;height:455px;background:linear-gradient(180deg,#dfe6ea 0%,#c9b9a3 45%,#8d8a80 62%,#2f8c96 80%,#1f6c78 100%)}
.play{left:870px;top:1567px;width:48px;height:48px;border-radius:50%;background:var(--orange);display:flex;align-items:center;justify-content:center}
.feature-title{left:109px;top:1460px;font-size:33px;font-weight:500;color:var(--navy)}
.f-row{left:109px;display:flex;align-items:center;gap:16px;font-size:18px}
.footer{left:0;top:1843px;width:1200px;height:410px;background:var(--soft)}
.f-head{font-size:13px;font-weight:700;color:var(--navy)}
.f-list{list-style:none;font-size:13px}
.f-list li{height:29.5px}
.phone-pill{left:624px;top:2031px;width:192px;height:40px;background:var(--white);border-radius:6px;box-shadow:0 4px 12px rgba(20,33,61,.06);display:flex;align-items:center;gap:8px;padding-left:14px}
.social{width:44px;height:44px;border-radius:50%;background:var(--navy)}
.social.hot{background:var(--orange);box-shadow:0 6px 14px rgba(240,78,10,.35)}
.legal{left:0;width:1200px;text-align:center}
</style>
</head>
<body>
<svg width="0" height="0" style="position:absolute">
  <defs>
    <symbol id="i-bed" viewBox="0 0 20 16"><path d="M2 14V3h16v11M2 10h16M5 7h4v3M11 7h4v3" fill="none" stroke="#7d8494" stroke-width="1.3"/></symbol>
    <symbol id="i-shower" viewBox="0 0 20 16"><path d="M10 1v3M3 8a7 4 0 0 1 14 0zM6 11v1M10 11v1M14 11v1M8 14v1M12 14v1" fill="none" stroke="#7d8494" stroke-width="1.3"/></symbol>
    <symbol id="i-garage" viewBox="0 0 20 16"><path d="M2 14V6l8-4 8 4v8M5 14V8h10v6M5 11h10" fill="none" stroke="#7d8494" stroke-width="1.3"/></symbol>
    <symbol id="i-dollar" viewBox="0 0 20 20"><circle cx="10" cy="10" r="8" fill="none" stroke="#f04e0a" stroke-width="1.5"/><path d="M12.5 7.5c-.5-1-1.5-1.3-2.5-1.3-1.5 0-2.4.8-2.4 1.8 0 2.5 5 1.3 5 3.9 0 1.1-1 1.9-2.6 1.9-1.1 0-2.100-.5-2.6-1.4M10 5v10" fill="none" stroke="#f04e0a" stroke-width="1.4"/></symbol>
    <symbol id="i-pin" viewBox="0 0 16 22"><path d="M8 21s7-7.5 7-12.5A7 7 0 0 0 1 8.5C1 13.5 8 21 8 21z" fill="none" stroke="#7d8494" stroke-width="1.3"/><circle cx="8" cy="8.5" r="1.3" fill="#7d8494"/></symbol>
    <symbol id="i-arrow" viewBox="0 0 18 10"><path d="M0 5h16M12 1l4 4-4 4" fill="none" stroke="#fff" stroke-width="1.5"/></symbol>
  </defs>
</svg>

<header class="abs header">
  <div class="abs brand" style="left:88px;top:36px"><span class="brand-dot"></span>BRONWICK HOMES</div>
  <div class="abs btn-outline" style="left:910px;top:23px;width:127px;height:41px">Contact us</div>
  <div class="abs menu-btn" style="left:1077px;top:26px">
    <svg width="14" height="10" viewBox="0 0 14 10"><path d="M0 1h14M0 5h14M0 9h14" stroke="#fff" stroke-width="1.2"/></svg>
  </div>
</header>

<div class="abs band"></div>
<h1 class="abs title">Bronwick properties</h1>
<div class="abs tab active" style="left:88px">
  <svg width="16" height="16" viewBox="0 0 16 16"><path d="M2 7l6-5 6 5v7H2z" fill="none" stroke="#fff" stroke-width="1.2"/><path d="M8 7v5" stroke="#fff" stroke-width="1.2"/></svg>In Sales</div>
<div class="abs tab plain" style="left:216px">
  <svg width="16" height="16" viewBox="0 0 16 16"><path d="M2 14V3l6 5 6-5v11M6 14v-4h4v4" fill="none" stroke="#14213d" stroke-width="1.2"/></svg>Sold</div>
<div class="abs script" style="left:888px;top:336px;font-size:22px;transform:rotate(-3deg)">Our super sexy properties</div>
<svg class="abs" style="left:848px;top:366px" width="40" height="48" viewBox="0 0 40 48"><path d="M36 4C20 4 10 14 9 40M4 34l5 8 6-7" fill="none" stroke="#f04e0a" stroke-width="1.5"/></svg>

<!-- Property grid -->
<div class="abs card" style="left:88px;top:447px">
  <div class="photo" role="img" aria-label="Bright open-plan living room with sofas and dining area" style="background:linear-gradient(160deg,#e9e4dc,#c8b59c 60%,#9a8670)"><div class="dots"><i></i><i></i><i></i><i></i></div></div>
  <div class="card-body"><div class="card-title">House Studio 1400 sqft</div>
    <div class="stats"><span class="stat"><svg width="20" height="16"><use href="#i-bed"/></svg>2</span><span class="stat"><svg width="20" height="16"><use href="#i-shower"/></svg>1</span><span class="stat"><svg width="20" height="16"><use href="#i-garage"/></svg>1</span></div>
    <div class="price"><svg width="18" height="18"><use href="#i-dollar"/></svg>$549,000</div></div>
  <div class="card-foot"><svg width="16" height="22"><use href="#i-pin"/></svg>14 Larkspur Lane, Wynmoor, Qld 4170</div>
</div>
<div class="abs card" style="left:449px;top:447px">
  <div class="photo" role="img" aria-label="Two-storey home with lit entrance and front garden at dusk" style="background:linear-gradient(180deg,#5b6a5e,#8e7a5c 50%,#4c7a2e)"><div class="dots"><i></i><i></i><i></i><i></i></div></div>
  <div class="card-body"><div class="card-title">2 Bhk house 1600 sqft</div>
    <div class="stats"><span class="stat"><svg width="20" height="16"><use href="#i-bed"/></svg>3</span><span class="stat"><svg width="20" height="16"><use href="#i-shower"/></svg>2</span><span class="stat"><svg width="20" height="16"><use href="#i-garage"/></svg>2</span></div>
    <div class="price"><svg width="18" height="18"><use href="#i-dollar"/></svg>$275,000</div></div>
  <div class="card-foot"><svg width="16" height="22"><use href="#i-pin"/></svg>VR/32 Halden Rd, West Arbury</div>
</div>
<div class="abs card" style="left:810px;top:447px">
  <div class="photo" role="img" aria-label="Front porch of a blue timber house with white wicker seating" style="background:linear-gradient(120deg,#1f2a3e,#6d87a6 45%,#c9d4dc 70%,#6f8f4a)"><div class="dots"><i></i><i></i><i></i><i></i></div></div>
  <div class="card-body"><div class="card-title">House 1500 sqft</div>
    <div class="stats"><span class="stat"><svg width="20" height="16"><use href="#i-bed"/></svg>1</span><span class="stat"><svg width="20" height="16"><use href="#i-shower"/></svg>1</span><span class="stat"><svg width="20" height="16"><use href="#i-garage"/></svg>1</span></div>
    <div class="price"><svg width="18" height="18"><use href="#i-dollar"/></svg>$215,000</div></div>
  <div class="card-foot"><svg width="16" height="22"><use href="#i-pin"/></svg>MC/88 Corrin St, Arbury City, Qld 4001</div>
</div>

<div class="abs card" style="left:88px;top:819px">
  <div class="photo" role="img" aria-label="Large timber farm house on a green lawn at sunset" style="background:linear-gradient(180deg,#b9a0b0,#d8b08c 40%,#6f7a3a 65%,#3f6a22)"><div class="dots"><i></i><i></i><i></i><i></i></div></div>
  <div class="card-body"><div class="card-title">Farm House 2400 sqft</div>
    <div class="stats"><span class="stat"><svg width="20" height="16"><use href="#i-bed"/></svg>2</span><span class="stat"><svg width="20" height="16"><use href="#i-shower"/></svg>1</span><span class="stat"><svg width="20" height="16"><use href="#i-garage"/></svg>1</span></div>
    <div class="price"><svg width="18" height="18"><use href="#i-dollar"/></svg>$549,000</div></div>
  <div class="card-foot"><svg width="16" height="22"><use href="#i-pin"/></svg>14 Larkspur Lane, Wynmoor, Qld 4170</div>
</div>
<div class="abs card" style="left:449px;top:819px">
  <div class="photo" role="img" aria-label="White modern kitchen with island bench and pendant lights" style="background:linear-gradient(180deg,#f2f2f0,#dedcd8 60%,#b8b4ae)"><div class="dots"><i></i><i></i><i></i><i></i></div></div>
  <div class="card-body"><div class="card-title">Dream house 2400 sqft</div>
    <div class="stats"><span class="stat"><svg width="20" height="16"><use href="#i-bed"/></svg>3</span><span class="stat"><svg width="20" height="16"><use href="#i-shower"/></svg>2</span><span class="stat"><svg width="20" height="16"><use href="#i-garage"/></svg>2</span></div>
    <div class="price"><svg width="18" height="18"><use href="#i-dollar"/></svg>$275,000</div></div>
  <div class="card-foot"><svg width="16" height="22"><use href="#i-pin"/></svg>VR/32 Halden Rd, West Arbury</div>
</div>
<div class="abs card" style="left:810px;top:819px">
  <div class="photo" role="img" aria-label="Cosy lounge room with sofa, coffee table and kitchen behind" style="background:linear-gradient(160deg,#c9c1b4,#8a6e55 55%,#5a4433)"><div class="dots"><i></i><i></i><i></i><i></i></div></div>
  <div class="card-body"><div class="card-title">House Studio 1400 sqft</div>
    <div class="stats"><span class="stat"><svg width="20" height="16"><use href="#i-bed"/></svg>2</span><span class="stat"><svg width="20" height="16"><use href="#i-shower"/></svg>1</span><span class="stat"><svg width="20" height="16"><use href="#i-garage"/></svg>1</span></div>
    <div class="price"><svg width="18" height="18"><use href="#i-dollar"/></svg>$215,000</div></div>
  <div class="card-foot"><svg width="16" height="22"><use href="#i-pin"/></svg>MC/88 Corrin St, Arbury City, Qld 4001</div>
</div>

<div class="abs btn-solid" style="left:494px;top:1201px;width:195px;height:65px;font-size:15px">Show more <svg width="18" height="10"><use href="#i-arrow"/></svg></div>

<!-- House of the week -->
<section class="abs feature"></section>
<div class="abs feature-photo" role="img" aria-label="Modern home with glass walls, outdoor kitchen and swimming pool"></div>
<div class="abs play"><svg width="14" height="16" viewBox="0 0 14 16"><path d="M1 1l12 7-12 7z" fill="#fff"/></svg></div>
<div class="abs script" style="left:109px;top:1436px;font-size:22px">House of the week</div>
<h2 class="abs feature-title">2 Bhk house 1600 sqft</h2>
<div class="abs f-row" style="top:1534px;gap:0;font-weight:500">
  <span class="stat" style="width:90px;gap:14px"><svg width="26" height="20"><use href="#i-bed"/></svg>3</span>
  <span class="stat" style="width:82px;gap:14px"><svg width="26" height="20"><use href="#i-shower"/></svg>2</span>
  <span class="stat" style="gap:14px"><svg width="26" height="20"><use href="#i-garage"/></svg>2</span>
</div>
<div class="abs f-row" style="top:1580px;color:var(--orange);font-weight:700"><svg width="22" height="22"><use href="#i-dollar"/></svg>$275,000</div>
<div class="abs f-row" style="top:1632px"><svg width="20" height="26"><use href="#i-pin"/></svg>VR/32 Halden Rd, West Arbury</div>
<div class="abs btn-solid" style="left:109px;top:1690px;width:131px;height:44px;font-size:13px">Contact us</div>

<!-- Footer -->
<footer class="abs footer"></footer>
<div class="abs brand" style="left:90px;top:1928px"><span class="brand-dot"></span>BRONWICK HOMES</div>
<div class="abs f-head" style="left:375px;top:1928px">Navigation</div>
<ul class="abs f-list" style="left:375px;top:1961px"><li>Home</li><li>About us</li><li>Properties</li><li>Contact</li></ul>
<div class="abs f-head" style="left:500px;top:1928px">Product</div>
<ul class="abs f-list" style="left:500px;top:1961px"><li>Property</li><li>Short stays</li><li>Finance</li><li>Reviews</li></ul>
<div class="abs f-head" style="left:624px;top:1928px">Adress</div>
<ul class="abs f-list" style="left:624px;top:1961px"><li>3/41 Elm St, Fernvale QLD 4071</li><li>hello@bronwickhomes.com.au</li></ul>
<div class="abs phone-pill">
  <svg width="16" height="16" viewBox="0 0 16 16"><circle cx="8" cy="8" r="8" fill="#20c1c9"/><path d="M5.5 4.5l1.5 1.8-.8 1a5 5 0 0 0 2.5 2.5l1-.8 1.8 1.5-.9 1.2c-3 0-6-3-6-6z" fill="#fff"/></svg>
  <span style="font-size:6px">Call us on</span><span style="font-size:10px;font-weight:700;letter-spacing:2px">0400-123-456</span>
</div>
<div class="abs f-head" style="left:896px;top:1928px">Social Media</div>
<div class="abs social" style="left:896px;top:1975px" aria-label="Social profile"></div>
<div class="abs social hot" style="left:957px;top:1975px" aria-label="Social profile"></div>
<div class="abs social" style="left:1014px;top:1975px" aria-label="Social profile"></div>
<div class="abs legal" style="top:2191px;font-size:11px;display:flex;justify-content:center;align-items:center;gap:6px">
  <svg width="14" height="14" viewBox="0 0 14 14"><circle cx="7" cy="7" r="6" fill="none" stroke="#1d2438"/><path d="M9 5.2A2.4 2.4 0 1 0 9 8.8" fill="none" stroke="#1d2438"/></svg>Bronwick Homes Company - All Rights Reserved</div>
<div class="abs legal" style="top:2215px;font-size:7.5px;color:var(--navy)">Terms &amp; Conditions | Privacy Policy | Compliance Policy | Contact Us</div>
</body>
</html>
```